T&R Custom Homes and Remodeling Flyer

We need a new double sided flyer that showcases our service.
Our website is http://trhomesbuildco.example/
Please use the information on http://trhomesbuildco.example/about-us/ for the information in the flyer.
This handout will be used to give to our potential customers and needs to show the complete story of who we are and the services we provide. I have also attached pictures of project we have completed that should be used for the flyer.
Any other pictures can be taken from our photo gallery on the website.

Target Market(s)

Clients who want a custom home or remodel

Industry/Entity Type

Construction

Font styles to use
Serif

Requirements
Must have
• Prominent logo
• Pictures of completed projects
• Tri-fold design- eps file is attached for this
Nice to have
• Manly colors
• If you can find a tasteful way to add the picture of the owners that is great, but it should be small and is not necessary.
Should not have
• Pink/girly touches

```html
<!DOCTYPE html>
<html lang="en">
<head>
<meta charset="utf-8">
<title>T&amp;R Custom Homes and Remodeling – Tri-fold Flyer</title>
<link rel="stylesheet" href="https://fonts.googleapis.com/css2?family=Oswald:wght@500;600&family=Arimo:wght@400;700&display=swap">
<style>
  :root{
    --stage:#2b2b2d;
    --charcoal:#3b3b3d;
    --charcoal-dark:#303032;
    --slate-blue:#4b6686;
    --navy:#2c4466;
    --paper:#ffffff;
    --ink:#222222;
    --soft-ink:#e6e6e6;
    --rule:#9aa3ad;
  }
  *{box-sizing:border-box;margin:0;padding:0}
  html,body{width:1200px;height:1200px;overflow:hidden}
  body{background:var(--stage);font-family:"Arimo",Arial,sans-serif;color:var(--ink);position:relative}
  .spread{position:absolute;left:30px;width:1140px;height:555px;display:flex;box-shadow:0 8px 24px rgba(0,0,0,.45)}
  .spread--outside{top:28px}
  .spread--inside{top:612px}
  .panel{width:380px;height:100%;position:relative;overflow:hidden;display:flex;flex-direction:column}
  .panel + .panel{border-left:1px solid rgba(0,0,0,.18)}
  .photo{width:100%;flex:none}
  .heading{font-family:"Oswald",Arial,sans-serif;font-weight:600;letter-spacing:.5px;text-transform:uppercase}
  .heading--light{color:var(--paper)}
  .heading--dark{color:var(--ink)}
  .heading-rule{height:1px;background:currentColor;opacity:.7;margin:4px 0 10px}
  .wordmark{font-family:"Arimo",Arial,sans-serif;font-weight:700;display:flex;align-items:center;gap:8px;justify-content:center;text-transform:uppercase}
  .wordmark__square{width:14px;height:14px;flex:none}

  /* outside: testimonials */
  .testimonials{background:var(--charcoal);flex:1;padding:16px 22px;color:var(--soft-ink)}
  .testimonials .heading{font-size:22px}
  .quote{font-size:10.5px;line-height:1.42;margin-bottom:10px}
  .quote cite{display:block;text-align:right;font-style:normal;font-weight:700;color:var(--paper);margin-top:2px}

  /* outside: welcome + contact */
  .welcome{background:var(--charcoal);padding:16px 26px 18px;color:var(--soft-ink);text-align:center}
  .welcome .wordmark{color:var(--paper);font-size:17px;margin-bottom:10px}
  .welcome p{font-size:10.5px;line-height:1.45;text-align:left}
  .contact{background:var(--slate-blue);flex:1;padding:20px 40px;color:var(--paper)}
  .contact .heading{font-size:26px}
  .contact__line{display:flex;align-items:center;gap:8px;font-size:11px;line-height:1.5;margin-bottom:5px}
  .contact__line svg{flex:none}
  .contact__company{font-size:13px;font-weight:700;margin-bottom:8px}

  /* outside: cover */
  .cover-brand{background:var(--paper);height:150px;display:flex;align-items:center;justify-content:center;border-top:14px solid var(--charcoal-dark)}
  .cover-brand .wordmark{color:var(--navy);font-size:22px;flex-direction:row}
  .cover-brand .wordmark small{display:block;font-size:11px;letter-spacing:2px}
  .cover-phone{background:var(--charcoal);height:60px;display:flex;align-items:center;justify-content:center;gap:12px;color:var(--paper);font-family:"Oswald",Arial,sans-serif;font-size:26px;font-weight:500}

  /* inside: about */
  .about{background:var(--paper);flex:1;padding:14px 24px 12px;position:relative}
  .about .heading{font-size:22px;text-align:center}
  .about p{font-size:10.3px;line-height:1.38;margin-bottom:7px}
  .about__signoff{font-size:11px;font-weight:700;line-height:1.4}
  .about .wordmark{position:absolute;right:22px;bottom:22px;font-size:11px;color:var(--navy)}

  /* inside: services */
  .photo-pair{display:flex;height:160px;gap:4px;background:var(--paper);padding:6px 6px 0}
  .photo-pair .photo{flex:1;height:100%;position:relative}
  .photo-tag{position:absolute;right:6px;font-size:9px;font-weight:700;color:var(--paper)}
  .services{background:var(--slate-blue);color:var(--paper);padding:14px 26px;height:205px}
  .services .heading{font-size:22px}
  .services ul{list-style:none;margin-bottom:8px}
  .services li{display:flex;align-items:center;gap:8px;font-size:11px;font-weight:700;text-transform:uppercase;line-height:1.75}
  .services p{font-size:10px;line-height:1.4}

  /* inside: gallery */
  .gallery{display:grid;grid-template-columns:1fr 1fr;grid-template-rows:150px 120px 1fr;gap:5px;background:var(--paper);padding:6px;height:100%}
  .gallery .photo{height:100%}
  .gallery .wide{grid-column:1 / 3}
</style>
</head>
<body>

<!-- OUTSIDE -->
<section class="spread spread--outside" aria-label="Flyer outside">
  <article class="panel panel--testimonials">
    <div class="photo" role="img" aria-label="Photo of a brick home porch with a white railing" style="height:170px;background:linear-gradient(135deg,#9a5a42,#d8d2c4 55%,#7d4433)"></div>
    <div class="testimonials">
      <h2 class="heading heading--light">Testimonials</h2>
      <div class="heading-rule"></div>
      <blockquote class="quote">“We had our basement finished by T&amp;R Custom Homes &amp; Remodeling last year, and although they came highly recommended, the work that they did exceeded all our expectations. Not only was there an incredible attention to detail, but the courtesy and service we received was superior. The basement looks fabulous and we couldn’t be happier.”<cite>- The Harlows, Maple Ridge IL</cite></blockquote>
      <blockquote class="quote">“We were very skeptical given our previous dealings; however, that feeling quickly subsided given T&amp;R’s approach to putting their customers first, their billing transparency and how every detail matters to them in the building process. I can honestly say that you cannot go wrong if you decided to build your custom dream home with T&amp;R Homes!”<cite>- Mark &amp; Dana Pruitt, Cedar Falls IL</cite></blockquote>
      <blockquote class="quote">“Six months ago we finished our basement and having T&amp;R Custom Homes &amp; Remodeling complete the job was one of the best decisions we had made. From the initial consultation to the final walk through, Tom listened to what we wanted, offered suggestions when we needed it and provided us with a professional insight that we could not have done without.”<cite>- Greg &amp; Lynn Halvorsen, Cedar Falls IL</cite></blockquote>
    </div>
  </article>

  <article class="panel panel--contact">
    <div class="photo" role="img" aria-label="Photo of a smiling family seated on the front steps of their new home" style="height:170px;background:linear-gradient(160deg,#7a4a38,#c9bfae 50%,#5c3a2c)"></div>
    <div class="welcome">
      <div class="wordmark"><span class="wordmark__square" style="background:var(--paper)"></span>T&amp;R Custom Homes</div>
      <p>Welcome to T&amp;R Custom Homes &amp; Remodeling, LLC serving the Chicago suburban area. The quality of T&amp;R shows in every detail. Our services range from new construction, to kitchen, bathroom and basement remodeling and everything in-between. T&amp;R approaches every project with an eye for detail and quality using exceptional craftsmanship combined with years of experience.</p>
    </div>
    <div class="contact">
      <h2 class="heading heading--light">Contact Us</h2>
      <div class="heading-rule"></div>
      <div class="contact__company">T &amp; R Homes LLC</div>
      <div class="contact__line">
        <svg width="12" height="12" viewBox="0 0 12 12" aria-hidden="true"><circle cx="6" cy="4" r="2.6" fill="#fff"/><path d="M1 12c0-3 2.3-4.6 5-4.6S11 9 11 12z" fill="#fff"/></svg>
        <span>1180 Birchwood Ave Suite 210<br>Fairview, IL 60999, USA</span>
      </div>
      <div class="contact__line">
        <svg width="12" height="12" viewBox="0 0 24 24" aria-hidden="true"><path d="M6.6 10.8a15.1 15.1 0 0 0 6.6 6.6l2.2-2.2a1 1 0 0 1 1-.25 11.4 11.4 0 0 0 3.6.57 1 1 0 0 1 1 1V20a1 1 0 0 1-1 1A17 17 0 0 1 3 4a1 1 0 0 1 1-1h3.5a1 1 0 0 1 1 1c0 1.25.2 2.45.57 3.57a1 1 0 0 1-.25 1z" fill="#fff"/></svg>
        <span>(555) 214-7730</span>
      </div>
      <div class="contact__line">
        <svg width="12" height="12" viewBox="0 0 12 12" aria-hidden="true"><path d="M6 11.5S1.5 7 1.5 4.5a4.5 4.5 0 0 1 9 0C10.5 7 6 11.5 6 11.5z" fill="#fff"/><circle cx="6" cy="4.5" r="1.6" fill="#4b6686"/></svg>
        <span>www.trhomesbuildco.example</span>
      </div>
    </div>
  </article>

  <article class="panel panel--cover">
    <div class="cover-brand">
      <div class="wordmark"><span class="wordmark__square" style="background:var(--navy)"></span><span>T&amp;R Custom Homes<small>and Remodeling</small></span></div>
    </div>
    <div class="photo" role="img" aria-label="Photo of a large brick custom home with a green lawn" style="flex:1;background:linear-gradient(180deg,#dbe6ee 0%,#a9806a 45%,#8a5f4a 70%,#4f7a36 85%,#3f6a2b 100%)"></div>
    <div class="cover-phone">
      <svg width="26" height="26" viewBox="0 0 26 26" aria-hidden="true"><circle cx="13" cy="13" r="11.5" fill="none" stroke="#fff" stroke-width="1.8"/><path d="M9.3 11.6a9 9 0 0 0 4 4l1.3-1.3a.6.6 0 0 1 .6-.15 6.8 6.8 0 0 0 2.1.34.6.6 0 0 1 .6.6v2.1a.6.6 0 0 1-.6.6A10 10 0 0 1 7.3 7.8a.6.6 0 0 1 .6-.6H10a.6.6 0 0 1 .6.6c0 .74.12 1.45.34 2.1a.6.6 0 0 1-.15.6z" fill="#fff"/></svg>
      (555) 214-7730
    </div>
  </article>
</section>

<!-- INSIDE -->
<section class="spread spread--inside" aria-label="Flyer inside">
  <article class="panel panel--about">
    <div class="photo" role="img" aria-label="Photo of the two company partners in black polo shirts" style="height:150px;background:linear-gradient(180deg,#d9cfc2,#b9ab99 55%,#1f1f21 56%,#2a2a2c)"></div>
    <div class="about">
      <h2 class="heading heading--dark">About Us</h2>
      <div class="heading-rule"></div>
      <p>With more than 20 years combined experience in construction, T&amp;R maintains the absolute highest levels of quality, material, workmanship, and service in each and every project we build.</p>
      <p>A reputation is only as great as the last referral and we understand that the future of our business relies upon satisfied customers. We take the time to fully understand our customer’s expectations. Customer service is more than just a trendy marketing theme, it is the underlying philosophy in everything we do and our home buyers reap the benefits of this philosophy.</p>
      <p>T&amp;R is committed to building quality homes with meticulous craftsmanship, custom designs, and thoughtful touches that add to the homeowners’ quality of life. Over the years, we have developed close working relationships with some of the best local craftsmen, vendors, and suppliers located in the western suburbs of Chicago.</p>
      <p>Throughout our experience we have developed lasting values of honesty, real quality, attention to fine detail, efficiency, timeliness, and most of all how to meet a customer’s expectation by asking the right questions.</p>
      <div class="about__signoff">Tom Reyes - Partner<br>Rick Alvarado - Partner</div>
      <div class="wordmark"><span class="wordmark__square" style="background:var(--navy)"></span>T&amp;R Custom Homes</div>
    </div>
  </article>

  <article class="panel panel--services">
    <div class="photo-pair">
      <div class="photo" role="img" aria-label="Photo of a finished kitchen island with bar stools" style="background:linear-gradient(160deg,#2f2c2a,#7a5134 60%,#a43a2c)"></div>
      <div class="photo" role="img" aria-label="Before and after photos of a remodeled front entry" style="background:linear-gradient(180deg,#9b8a78 0%,#c9c2b6 49%,#ffffff 49.5%,#ffffff 50.5%,#6d6a66 51%,#b5aca0 100%)">
        <span class="photo-tag" style="top:58px">AFTER</span>
        <span class="photo-tag" style="bottom:6px">BEFORE</span>
      </div>
    </div>
    <div class="services">
      <h2 class="heading heading--light">Our Services</h2>
      <div class="heading-rule"></div>
      <ul>
        <li><svg width="14" height="14" viewBox="0 0 14 14" aria-hidden="true"><circle cx="7" cy="7" r="7" fill="#fff"/><path d="M3.8 7.2l2.2 2.2 4.2-4.4" fill="none" stroke="#4b6686" stroke-width="1.8"/></svg>Construction (All Types)</li>
        <li><svg width="14" height="14" viewBox="0 0 14 14" aria-hidden="true"><circle cx="7" cy="7" r="7" fill="#fff"/><path d="M3.8 7.2l2.2 2.2 4.2-4.4" fill="none" stroke="#4b6686" stroke-width="1.8"/></svg>Remodeling</li>
        <li><svg width="14" height="14" viewBox="0 0 14 14" aria-hidden="true"><circle cx="7" cy="7" r="7" fill="#fff"/><path d="M3.8 7.2l2.2 2.2 4.2-4.4" fill="none" stroke="#4b6686" stroke-width="1.8"/></svg>Building-Related Services</li>
      </ul>
      <p>Let T&amp;R Homes be a part of your next construction project...you’ll be happy that you did.</p>
      <p>Whether the job is big or small, T&amp;R promise one-on-one service with customer satisfaction guaranteed.</p>
    </div>
    <div class="photo" role="img" aria-label="Photo of a bright kitchen with white cabinets and stainless appliances" style="flex:1;background:linear-gradient(170deg,#e8e3da,#b9a58c 45%,#f2f0ea 70%,#5a4232)"></div>
  </article>

  <article class="panel panel--gallery">
    <div class="gallery">
      <div class="photo wide" role="img" aria-label="Photo of a two-story foyer with a chandelier and hardwood floors" style="background:linear-gradient(170deg,#efe9dd,#cbbfa9 60%,#4a3326)"></div>
      <div class="photo" role="img" aria-label="Photo of a room with a blue accent wall" style="background:linear-gradient(150deg,#e6e0d4,#2c5aa0 50%,#6b4a34)"></div>
      <div class="photo" role="img" aria-label="Photo of dark wood kitchen cabinets and a tiled backsplash" style="background:linear-gradient(150deg,#d9d2c5,#3b2a22 50%,#6e6a66)"></div>
      <div class="photo wide" role="img" aria-label="Photo of a kitchen with dark cabinets and a large island" style="background:linear-gradient(170deg,#e9e5de,#8e7762 40%,#2f241d 75%,#6a4b35)"></div>
    </div>
  </article>
</section>

</body>
</html>
```